Stationary and Business Card for dental office
Velbrook Endodontics
Stationary and Business Card for dental office  - Health
Creative Brief
Use same font as used in my logo
use any font that is easy to read. should go with font in the logo
Professional
Miren T. Osbury, D.D.S.
418 Pelloway Court, Suite #1 Manteca, CA 95337
info@velbrookendo.example
www.velbrookendo.example
Business card should have 2 logos, one brown and gold one with a tooth image....that is my main logo. The second logo( the one that says pdrcertified member) which I have uploaded as well can be in a corner or anywhere on the card. basically it is your choice where it goes on the card. It does not have to be the same size as my main business logo. This second logo only needs to be on the business cards. it can be black and white or color. I will leave that decision to you so if you think the colored logo goes with my logo colors, then use that. If not then, use the black and white one. I will prefer it in color. Under my name on business card, please write the following in smaller font Practice Limited to Endodontics LETTER HEAD: deisgn does not need to have the second logo (pdrcertifeid member logo). It should have my main business logo ( gold and brown one) with business name and all the other info like address, phone, fax web/email. ENVELOPE: only main business logo with business name and address. Please do not include phone/fax/ email or any other logos on the envelope. Thank you.

```html
<!DOCTYPE html>
<html lang="en">
<head>
<meta charset="utf-8">
<title>Velbrook Endodontics – Business Card</title>
<link rel="stylesheet" href="https://fonts.googleapis.com/css2?family=Cormorant+Garamond:wght@600&family=Open+Sans:wght@400;600&display=swap">
<style>
  :root {
    --backdrop: #2b2b2d;
    --card-white: #ffffff;
    --brown: #5b3b27;
    --brown-deep: #4a2f1f;
    --gold: #b08a5e;
    --ink-light: #f4ece2;
    --ink-dark: #4a3020;
    --badge-fill: #e9e5e0;
  }
  * { box-sizing: border-box; margin: 0; padding: 0; }
  html, body { width: 1200px; height: 969px; overflow: hidden; }
  body {
    background: var(--backdrop);
    display: flex;
    flex-direction: column;
    align-items: center;
    justify-content: center;
    gap: 48px;
    font-family: "Open Sans", Arial, sans-serif;
  }
  .card {
    width: 740px;
    height: 423px;
    background: var(--card-white);
    position: relative;
    overflow: hidden;
    box-shadow: 0 10px 30px rgba(0,0,0,0.45);
  }

  /* Card back: centred brand mark */
  .card-back {
    display: flex;
    flex-direction: column;
    align-items: center;
    justify-content: center;
    gap: 22px;
  }
  .brand-dot {
    border-radius: 50%;
    background: var(--gold);
  }
  .card-back .brand-dot { width: 150px; height: 150px; }
  .brand-name {
    font-family: "Cormorant Garamond", Georgia, serif;
    font-weight: 600;
    color: var(--ink-dark);
    letter-spacing: 0.3px;
  }
  .card-back .brand-name { font-size: 40px; }

  /* Card front: white identity column + brown contact panel */
  .card-front { display: flex; }
  .identity {
    width: 42%;
    display: flex;
    flex-direction: column;
    align-items: center;
    padding: 58px 24px 0;
  }
  .identity .brand-dot { width: 96px; height: 96px; }
  .identity .brand-name { font-size: 26px; margin-top: 16px; white-space: nowrap; }
  .member-badge {
    margin-top: 34px;
    width: 56px;
    height: 56px;
    border-radius: 50%;
    border: 3px solid var(--ink-dark);
    background: var(--badge-fill);
  }
  .member-label {
    margin-top: 8px;
    font-size: 10px;
    font-weight: 600;
    letter-spacing: 1.5px;
    text-transform: uppercase;
    color: #222;
  }
  .contact-panel {
    width: 58%;
    background: linear-gradient(to bottom, var(--brown) 0%, var(--brown-deep) 100%);
    color: var(--ink-light);
    text-align: right;
    padding: 40px 34px 0 20px;
  }
  .doctor-name { font-size: 20px; font-weight: 400; letter-spacing: 0.3px; }
  .practice-note { font-size: 12px; margin-top: 2px; }
  .contact-list { margin-top: 46px; font-size: 13.5px; line-height: 1.5; list-style: none; }
  .contact-list .gap { margin-top: 14px; }
</style>
</head>
<body>
  <section class="card card-back">
    <div class="brand-dot" aria-hidden="true"></div>
    <div class="brand-name">Velbrook Endodontics</div>
  </section>

  <section class="card card-front">
    <div class="identity">
      <div class="brand-dot" aria-hidden="true"></div>
      <div class="brand-name">Velbrook Endodontics</div>
      <div class="member-badge" role="img" aria-label="Specialist membership badge"></div>
      <div class="member-label">Specialist Member</div>
    </div>
    <div class="contact-panel">
      <div class="doctor-name">Miren T. Osbury, D.D.S.</div>
      <div class="practice-note">Practice Limited to Endodontics</div>
      <ul class="contact-list">
        <li>418 Pelloway Court, Suite #1</li>
        <li>Manteca, CA 95337</li>
        <li>Tel: 209-555-0142</li>
        <li>Fax: 209-555-0187</li>
        <li class="gap">Email: info@velbrookendo.example</li>
        <li>www.velbrookendo.example</li>
      </ul>
    </div>
  </section>
</body>
</html>
```